Morvela Aesthetic Doctor

I require an elegant, luxurious looking business card for my aesthetic business. I am a doctor and that will set me aside from competitors. I am planning to provide home and spa based treatments to clients with high expectations. I have attached my logo.

```html
<!DOCTYPE html>
<html lang="en">
<head>
<meta charset="utf-8">
<title>Morvela Aesthetic Doctor – Business Card</title>
<link rel="stylesheet" href="https://fonts.googleapis.com/css2?family=Open+Sans:wght@300;400;600&display=swap">
<style>
  :root {
    --card-white: #ffffff;
    --panel-blue: #d4e9f5;
    --ink: #1f1f1f;
    --accent-blue: #5fb3dd;
    --logo-blue: #7aa8c4;
    --icon-blue: #7cc0e4;
  }
  html, body {
    margin: 0;
    padding: 0;
    width: 1200px;
    height: 742px;
    overflow: hidden;
    background: var(--card-white);
    font-family: "Open Sans", Arial, sans-serif;
    color: var(--ink);
  }
  .card {
    position: relative;
    width: 1200px;
    height: 742px;
    background: var(--card-white);
  }
  .service-panel {
    position: absolute;
    left: 719px;
    top: 0;
    width: 481px;
    height: 742px;
    background: var(--panel-blue);
  }
  .doctor-name {
    position: absolute;
    left: 80px;
    top: 128px;
    margin: 0;
    font-size: 42px;
    font-weight: 400;
    letter-spacing: 0.2px;
    white-space: nowrap;
  }
  .doctor-name .credentials {
    font-size: 24px;
    letter-spacing: 0.5px;
  }
  .qualification {
    position: absolute;
    left: 80px;
    top: 180px;
    margin: 0;
    font-size: 22px;
    font-variant: small-caps;
    color: var(--accent-blue);
    letter-spacing: 0.6px;
    white-space: nowrap;
  }
  .contact-list {
    position: absolute;
    left: 76px;
    top: 270px;
    margin: 0;
    padding: 0;
    list-style: none;
  }
  .contact-list li {
    display: flex;
    align-items: center;
    height: 65.5px;
    font-size: 28px;
    font-weight: 400;
  }
  .contact-icon {
    width: 48px;
    height: 40px;
    margin-right: 32px;
    flex: none;
  }
  .contact-icon * {
    fill: none;
    stroke: var(--icon-blue);
    stroke-width: 2;
  }
  .brand {
    position: absolute;
    left: 790px;
    top: 118px;
    display: flex;
    align-items: center;
  }
  .brand-dot {
    width: 54px;
    height: 54px;
    border-radius: 50%;
    background: var(--logo-blue);
    margin-right: 20px;
    flex: none;
  }
  .brand-name {
    font-size: 30px;
    font-weight: 300;
    color: var(--logo-blue);
    line-height: 1.15;
    letter-spacing: 1px;
  }
  .service-list {
    position: absolute;
    right: 93px;
    top: 270px;
    margin: 0;
    padding: 0;
    list-style: none;
    text-align: right;
  }
  .service-list li {
    height: 65.5px;
    line-height: 65.5px;
    font-size: 28px;
    font-weight: 400;
  }
</style>
</head>
<body>
<main class="card">
  <div class="service-panel"></div>

  <h1 class="doctor-name">Dr Lianne Corvell <span class="credentials">MRCPCH MD</span></h1>
  <p class="qualification">Australasian Diploma of Aesthetic Medicine</p>

  <ul class="contact-list">
    <li>
      <svg class="contact-icon" viewBox="0 0 48 40" aria-hidden="true">
        <rect x="15" y="3" width="18" height="34" rx="3"/>
        <line x1="21" y1="31" x2="27" y2="31"/>
      </svg>
      0800 555 014
    </li>
    <li>
      <svg class="contact-icon" viewBox="0 0 48 40" aria-hidden="true">
        <rect x="5" y="8" width="38" height="25" rx="1"/>
        <polyline points="5,8 24,23 43,8"/>
      </svg>
      lianne@morvela.co.nz
    </li>
    <li>
      <svg class="contact-icon" viewBox="0 0 48 40" aria-hidden="true">
        <circle cx="24" cy="20" r="16"/>
        <ellipse cx="24" cy="20" rx="7" ry="16"/>
        <line x1="8" y1="20" x2="40" y2="20"/>
        <path d="M11 12 H37 M11 28 H37"/>
      </svg>
      www.morvela.co.nz
    </li>
    <li>
      <svg class="contact-icon" viewBox="0 0 48 40" aria-hidden="true">
        <circle cx="24" cy="20" r="13"/>
      </svg>
      dr_lianne_corvell
    </li>
    <li>
      <svg class="contact-icon" viewBox="0 0 48 40" aria-hidden="true">
        <rect x="11" y="7" width="26" height="26" rx="7"/>
      </svg>
      dr_lianne_corvell
    </li>
  </ul>

  <div class="brand">
    <span class="brand-dot"></span>
    <span class="brand-name">Morvela<br>Aesthetic Doctor</span>
  </div>

  <ul class="service-list">
    <li>Dermal injectables</li>
    <li>Plasma facials</li>
    <li>Microneedling</li>
    <li>Skin boosters</li>
    <li>Excessive sweating</li>
  </ul>
</main>
</body>
</html>
```